Overview of User Roles and their Functions

I need an overview of user roles and their functions. It should be presented on a A4 page to be shown during customer visits, but also put into our company presentation if possible.
I made a drawing with the information which needs to be mentioned (if it is not properly readable, please let me know)
The user roles are for our webportal Vendra-x Hub. To explain briefly: a producer can upload documents, and share them with distributors, who can use the same system to share documents with their customers. But a producer can also share documents directly with customers.
If you find a possibility to show these connections, may be with a document flying over to the right places, please try to implement this thought. Or additionally for the function: generate customer notification an email flying over to the distributor and customer. This could be flying over the top of the graph or underneath, or through it all, whatever works better without looking overloaded.
Producer and Distributor + are chargeable user accounts (you could add chargeable right underneath the title)
For the free distributor role I thought, this could all be slightly greyed out and have the Distributor + in more attractive colors. Producer and Customer can both be in attractive colors which stand out.
I tried to list the functions which are the same for different roles all on one line. May be you have a good idea about how not to let it look empty where there is no function mentioned?
Because I didn't have enough space, I didn't write docs properly as documents, or req.s as requests. Please choose a size where it is possible to write out the whole word.
as a background or generally, please use similar colors like on my website www.vendraxhub.example . To make something stand out, you can also use different colors.
Please let me know if you have any additional questions. I am happy to answer them...
Target Market(s)
Pharmaceutical
Industry/Entity Type
Pharmaceutical
Font styles to use
Other font styles liked:
- if it is possible please use Raleway but if with Raleway the overview or readability is bad, use your own selected
Requirements
Must have
- clear overview of functions but if somehow possible, also show the connection the user roles can have with each other

```html
<!DOCTYPE html>
<html lang="en">
<head>
<meta charset="utf-8">
<title>Vendra-x Hub User Roles</title>
<link href="https://fonts.googleapis.com/css2?family=Maven+Pro:wght@500;600;700&family=Raleway:ital,wght@0,400;0,500;1,400&display=swap" rel="stylesheet">
<style>
  :root{
    --brand:#0d57a5;
    --brand-dark:#0a4a8e;
    --header-band:#ededef;
    --panel:#f7f7f8;
    --stripe:#e9e9ec;
    --producer:#29a3dc;
    --distributor:#0d64ad;
    --distplus:#2e2a8c;
    --customer:#251f5e;
    --tick-producer:#27a8e0;
    --tick-distributor:#1a6ab0;
    --tick-distplus:#2f2d8a;
    --tick-customer:#151515;
    --dash:#b9b9bd;
  }
  *{box-sizing:border-box;margin:0;padding:0}
  html,body{width:1200px;height:887px;overflow:hidden;background:#fff}
  .sheet{position:relative;width:1200px;height:887px;background:#fff;overflow:hidden;font-family:"Raleway",sans-serif}
  .header-band{position:absolute;left:0;top:0;width:1200px;height:160px;background:var(--header-band)}
  .title{position:absolute;left:98px;top:30px;font-family:"Maven Pro",sans-serif;font-weight:600;font-size:58px;color:var(--brand);letter-spacing:-.3px;white-space:nowrap}
  .website{position:absolute;left:107px;top:94px;font-family:"Raleway",sans-serif;font-size:28px;color:#1b1b1b}
  .brand-mark{position:absolute;left:846px;top:50px;display:flex;align-items:center;gap:12px}
  .brand-mark .dot{width:56px;height:56px;border-radius:50%;background:var(--brand)}
  .brand-mark .name{font-family:"Maven Pro",sans-serif;font-weight:600;font-size:40px;color:var(--brand);letter-spacing:.5px}
  .bottom-band{position:absolute;left:0;top:663px;width:1200px;height:224px;background:var(--brand)}
  .panel{position:absolute;left:76px;top:160px;width:1049px;height:675px;background:var(--panel);box-shadow:0 4px 14px rgba(0,0,0,.18)}
  .matrix{position:absolute;left:105px;top:206px;width:992px}
  .row{display:grid;grid-template-columns:284px 174px 174px 174px 174px;column-gap:3px;height:37.4px}
  .pricing{height:32px;align-items:center}
  .pricing span{text-align:center;font-family:"Maven Pro",sans-serif;font-weight:500;font-size:20px;color:var(--brand)}
  .role-head{height:48px}
  .role-head div{display:flex;align-items:center;justify-content:center;font-family:"Maven Pro",sans-serif;font-weight:600;font-size:23px;color:#fff}
  .role-head .functions-title{background:var(--brand);font-size:25px;justify-content:flex-start;padding-left:46px}
  .role-head .producer{background:var(--producer)}
  .role-head .distributor{background:var(--distributor)}
  .role-head .distplus{background:var(--distplus)}
  .role-head .customer{background:var(--customer)}
  .function{position:relative;background:var(--brand);border-top:1px solid var(--brand-dark);display:flex;align-items:center;padding-left:22px;color:#fff;font-size:14.5px;font-weight:500}
  .function::after{content:"";position:absolute;right:-7px;top:50%;margin-top:-6px;border-left:7px solid var(--brand);border-top:6px solid transparent;border-bottom:6px solid transparent;z-index:1}
  .function svg{width:22px;height:22px;margin-right:12px;flex:none;fill:none;stroke:#fff;stroke-width:1.4;stroke-linecap:round;stroke-linejoin:round}
  .cell{display:flex;align-items:center;justify-content:center}
  .row:nth-child(even) .cell{background:var(--stripe)}
  .tick{width:23px;height:23px}
  .producer-col{color:var(--tick-producer)}
  .distributor-col{color:var(--tick-distributor)}
  .distplus-col{color:var(--tick-distplus)}
  .customer-col{color:var(--tick-customer)}
  .dash{width:27px;height:3px;background:var(--dash);border-radius:1px}
  .note{gap:8px}
  .note small{font-style:italic;font-size:9.5px;line-height:1.2;color:#1b1b1b;text-align:center}
</style>
</head>
<body>
<svg width="0" height="0" style="position:absolute" aria-hidden="true">
  <defs>
    <symbol id="tick" viewBox="0 0 24 24">
      <circle cx="12" cy="12" r="12" fill="currentColor"/>
      <path d="M7 12.5l3.3 3.2L17 9" fill="none" stroke="#fff" stroke-width="2" stroke-linecap="round" stroke-linejoin="round"/>
    </symbol>
  </defs>
</svg>
<div class="sheet">
  <div class="header-band"></div>
  <h1 class="title">Vendra-x Hub User Roles</h1>
  <p class="website">www.vendraxhub.example</p>
  <div class="brand-mark"><span class="dot"></span><span class="name">VENDRA-X</span></div>

  <div class="bottom-band"></div>
  <div class="panel"></div>

  <div class="matrix">
    <div class="row pricing"><span></span><span>Chargeable</span><span>FREE</span><span>Chargeable</span><span>FREE</span></div>
    <div class="row role-head">
      <div class="functions-title">User Functions</div>
      <div class="producer">Producer</div>
      <div class="distributor">Distributor</div>
      <div class="distplus">Distributor +</div>
      <div class="customer">Custsomer</div>
    </div>

    <div class="rows">
      <div class="row">
        <div class="function"><svg viewBox="0 0 24 24"><path d="M7 18H6a4 4 0 0 1 0-8 6 6 0 0 1 11.5-1A4.5 4.5 0 0 1 18 18h-1"/><path d="M12 20v-8M9 15l3-3 3 3"/></svg>Upload Documents</div>
        <div class="cell producer-col"><svg class="tick"><use href="#tick"/></svg></div>
        <div class="cell"><span class="dash"></span></div>
        <div class="cell distplus-col"><svg class="tick"><use href="#tick"/></svg></div>
        <div class="cell"><span class="dash"></span></div>
      </div>
      <div class="row">
        <div class="function"><svg viewBox="0 0 24 24"><circle cx="17" cy="5" r="2.5"/><circle cx="6" cy="12" r="2.5"/><circle cx="17" cy="19" r="2.5"/><path d="M8.3 10.8l6.4-4.4M8.3 13.2l6.4 4.4"/></svg>Share</div>
        <div class="cell note producer-col"><svg class="tick"><use href="#tick"/></svg><small>(directly share<br>with customers)</small></div>
        <div class="cell distributor-col"><svg class="tick"><use href="#tick"/></svg></div>
        <div class="cell distplus-col"><svg class="tick"><use href="#tick"/></svg></div>
        <div class="cell"><span class="dash"></span></div>
      </div>
      <div class="row">
        <div class="function"><svg viewBox="0 0 24 24"><path d="M7 16H6a4 4 0 0 1 0-8 6 6 0 0 1 11.5-1A4.5 4.5 0 0 1 18 16h-1"/><path d="M12 11v10M9 18l3 3 3-3"/></svg>Download Docs</div>
        <div class="cell"><span class="dash"></span></div>
        <div class="cell distributor-col"><svg class="tick"><use href="#tick"/></svg></div>
        <div class="cell distplus-col"><svg class="tick"><use href="#tick"/></svg></div>
        <div class="cell customer-col"><svg class="tick"><use href="#tick"/></svg></div>
      </div>
      <div class="row">
        <div class="function"><svg viewBox="0 0 24 24"><path d="M7 18H6a4 4 0 0 1 0-8 6 6 0 0 1 11.5-1A4.5 4.5 0 0 1 18 18h-1"/><path d="M12 20v-8M9 15l3-3 3 3"/></svg>Upload COAS</div>
        <div class="cell producer-col"><svg class="tick"><use href="#tick"/></svg></div>
        <div class="cell"><span class="dash"></span></div>
        <div class="cell"><span class="dash"></span></div>
        <div class="cell"><span class="dash"></span></div>
      </div>
      <div class="row">
        <div class="function"><svg viewBox="0 0 24 24"><path d="M6 16V11a6 6 0 0 1 12 0v5l2 2H4z"/><path d="M10 20a2 2 0 0 0 4 0"/></svg>Generate Customer Notifications</div>
        <div class="cell producer-col"><svg class="tick"><use href="#tick"/></svg></div>
        <div class="cell"><span class="dash"></span></div>
        <div class="cell distplus-col"><svg class="tick"><use href="#tick"/></svg></div>
        <div class="cell"><span class="dash"></span></div>
      </div>
      <div class="row">
        <div class="function"><svg viewBox="0 0 24 24"><rect x="4" y="3" width="16" height="14"/><path d="M7 7h10M7 10h10M7 13h6M12 17v5M9.5 19.5L12 22l2.5-2.5"/></svg>Receive Notifications</div>
        <div class="cell"><span class="dash"></span></div>
        <div class="cell distributor-col"><svg class="tick"><use href="#tick"/></svg></div>
        <div class="cell distplus-col"><svg class="tick"><use href="#tick"/></svg></div>
        <div class="cell customer-col"><svg class="tick"><use href="#tick"/></svg></div>
      </div>
      <div class="row">
        <div class="function"><svg viewBox="0 0 24 24"><circle cx="10" cy="10" r="6.5"/><path d="M15 15l6 6"/></svg>View other Listed Supplies</div>
        <div class="cell"><span class="dash"></span></div>
        <div class="cell distributor-col"><svg class="tick"><use href="#tick"/></svg></div>
        <div class="cell distplus-col"><svg class="tick"><use href="#tick"/></svg></div>
        <div class="cell customer-col"><svg class="tick"><use href="#tick"/></svg></div>
      </div>
      <div class="row">
        <div class="function"><svg viewBox="0 0 24 24"><path d="M19 12v8H4V5h9"/><path d="M8 11l3.5 3.5L20 5"/></svg>Receive access requests</div>
        <div class="cell producer-col"><svg class="tick"><use href="#tick"/></svg></div>
        <div class="cell"><span class="dash"></span></div>
        <div class="cell"><span class="dash"></span></div>
        <div class="cell"><span class="dash"></span></div>
      </div>
      <div class="row">
        <div class="function"><svg viewBox="0 0 24 24"><path d="M8 5V3h8v2"/><rect x="4" y="5" width="16" height="16"/><circle cx="12" cy="11" r="2"/><path d="M12 13v4"/></svg>Request Access</div>
        <div class="cell"><span class="dash"></span></div>
        <div class="cell distributor-col"><svg class="tick"><use href="#tick"/></svg></div>
        <div class="cell distplus-col"><svg class="tick"><use href="#tick"/></svg></div>
        <div class="cell customer-col"><svg class="tick"><use href="#tick"/></svg></div>
      </div>
      <div class="row">
        <div class="function"><svg viewBox="0 0 24 24"><rect x="3" y="3" width="18" height="18"/><path d="M13 7h4v4M17 7l-6 6M11 17H7v-4"/></svg>Versioning System</div>
        <div class="cell note producer-col"><svg class="tick"><use href="#tick"/></svg><small>(View difference<br>between old/new file)</small></div>
        <div class="cell distributor-col"><svg class="tick"><use href="#tick"/></svg></div>
        <div class="cell distplus-col"><svg class="tick"><use href="#tick"/></svg></div>
        <div class="cell customer-col"><svg class="tick"><use href="#tick"/></svg></div>
      </div>
      <div class="row">
        <div class="function"><svg viewBox="0 0 24 24"><circle cx="6" cy="6" r="3.5"/><path d="M6 4.5V6l1 1M13 5l8 15H7z M14 11v4M14 17.5v.3"/></svg>Expiry Notification</div>
        <div class="cell producer-col"><svg class="tick"><use href="#tick"/></svg></div>
        <div class="cell"><span class="dash"></span></div>
        <div class="cell distplus-col"><svg class="tick"><use href="#tick"/></svg></div>
        <div class="cell"><span class="dash"></span></div>
      </div>
      <div class="row">
        <div class="function"><svg viewBox="0 0 24 24"><path d="M6 2h9l4 4v16H6z"/><path d="M9 10h7M9 13h7M9 16h7M9 19h5"/></svg>Reports</div>
        <div class="cell producer-col"><svg class="tick"><use href="#tick"/></svg></div>
        <div class="cell"><span class="dash"></span></div>
        <div class="cell distplus-col"><svg class="tick"><use href="#tick"/></svg></div>
        <div class="cell"><span class="dash"></span></div>
      </div>
      <div class="row">
        <div class="function"><svg viewBox="0 0 24 24"><path d="M8 2h12v18"/><rect x="4" y="5" width="13" height="17"/><circle cx="10.5" cy="13" r="4"/><path d="M10.5 11v2l1.5 1"/></svg>Automated emailed Reports</div>
        <div class="cell producer-col"><svg class="tick"><use href="#tick"/></svg></div>
        <div class="cell"><span class="dash"></span></div>
        <div class="cell distplus-col"><svg class="tick"><use href="#tick"/></svg></div>
        <div class="cell"><span class="dash"></span></div>
      </div>
      <div class="row">
        <div class="function"><svg viewBox="0 0 24 24"><path d="M10 3h4v10h6v5H4v-5h6z"/><path d="M3 21h18"/></svg>Set stamps on docs</div>
        <div class="cell producer-col"><svg class="tick"><use href="#tick"/></svg></div>
        <div class="cell"><span class="dash"></span></div>
        <div class="cell distplus-col"><svg class="tick"><use href="#tick"/></svg></div>
        <div class="cell"><span class="dash"></span></div>
      </div>
    </div>
  </div>
</div>
</body>
</html>
```